Property developer, money partner needs business card design using logo concept provided

Our company develops residential properties, does money lends for joint ventures in property deals and finds property deals for other money partners. We have provided a basic logo for you to work from. Any graphic or logo design on the card is to communicate development and finance collaboration. Color choice is not so important for us, but color choice does need to reflect professionalism.

```html
<!DOCTYPE html>
<html lang="en">
<head>
<meta charset="utf-8">
<title>Keystone Property Partners – Business Card</title>
<link rel="stylesheet" href="https://fonts.googleapis.com/css2?family=Open+Sans:wght@400;600;700&display=swap">
<style>
  :root {
    --page-bg: #e4e6e9;
    --card-bg: #ffffff;
    --card-shade: #eceef0;
    --brand-blue: #1d4fa0;
    --brand-navy: #1a3a82;
    --name-blue: #1f7bc4;
    --accent-red: #b3282d;
    --text-grey: #5a5a5a;
    --text-dark: #222222;
  }
  * { box-sizing: border-box; margin: 0; padding: 0; }
  html, body {
    width: 1200px; height: 900px; overflow: hidden;
    background: var(--page-bg);
    font-family: "Open Sans", Arial, sans-serif;
  }
  .sheet {
    width: 1200px; height: 900px;
    display: flex; flex-direction: column;
    align-items: center; justify-content: center; gap: 48px;
  }
  .card {
    position: relative;
    width: 700px; height: 400px;
    background: linear-gradient(115deg, var(--card-shade) 0%, var(--card-bg) 55%);
    box-shadow: 0 8px 22px rgba(0,0,0,.18);
    overflow: hidden;
  }
  .card__band {
    position: absolute; left: 0; right: 0; bottom: 0;
    height: 16px; background: var(--brand-blue);
  }
  .brand {
    position: absolute; right: 60px; top: 70px;
    display: flex; flex-direction: column; align-items: flex-end;
    line-height: 1.3;
  }
  .brand__row { display: flex; align-items: center; gap: 14px; }
  .brand__dot {
    width: 44px; height: 44px; border-radius: 50%;
    background: var(--brand-blue);
  }
  .brand__name {
    font-weight: 700; font-size: 34px; letter-spacing: 4px;
    color: var(--brand-navy); text-transform: uppercase;
  }
  .brand__tagline {
    margin-top: 4px; font-size: 17px; letter-spacing: 3px; color: var(--text-dark);
  }
  .brand__acn {
    margin-top: 2px; font-size: 12px; letter-spacing: 2px; color: var(--text-dark);
  }
  .contact-card .brand { top: 40px; right: 50px; }
  .person {
    position: absolute; left: 60px; top: 170px;
    line-height: 1.35;
  }
  .person__name {
    font-size: 22px; font-weight: 600; color: var(--name-blue);
    letter-spacing: .5px; text-transform: uppercase;
  }
  .person__role { font-size: 17px; color: var(--text-grey); }
  .contacts {
    list-style: none; margin-top: 16px;
    display: flex; flex-direction: column; gap: 4px;
  }
  .contacts li {
    display: flex; align-items: center; gap: 12px;
    font-size: 16px; color: var(--text-grey);
  }
  .contacts svg { width: 16px; height: 16px; fill: var(--accent-red); flex: none; }
</style>
</head>
<body>
<main class="sheet">

  <section class="card front-card">
    <div class="brand">
      <div class="brand__row">
        <span class="brand__dot"></span>
        <span class="brand__name">Keystone</span>
      </div>
      <span class="brand__tagline">Property Partners</span>
      <span class="brand__acn">A.C.N 418 203 776</span>
    </div>
    <div class="card__band"></div>
  </section>

  <section class="card contact-card">
    <div class="brand">
      <div class="brand__row">
        <span class="brand__dot"></span>
        <span class="brand__name">Keystone</span>
      </div>
      <span class="brand__tagline">Property Partners</span>
      <span class="brand__acn">A.C.N 418 203 776</span>
    </div>

    <div class="person">
      <h1 class="person__name">Daniel Harlow</h1>
      <p class="person__role">Director</p>
      <ul class="contacts">
        <li>
          <svg viewBox="0 0 24 24" aria-hidden="true"><path d="M6.6 10.8a15.2 15.2 0 0 0 6.6 6.6l2.2-2.2a1 1 0 0 1 1-.25 11.4 11.4 0 0 0 3.6.57 1 1 0 0 1 1 1V20a1 1 0 0 1-1 1A17 17 0 0 1 3 4a1 1 0 0 1 1-1h3.5a1 1 0 0 1 1 1c0 1.250.2 2.45.57 3.57a1 1 0 0 1-.25 1z"/></svg>
          300-410-7725
        </li>
        <li>
          <svg viewBox="0 0 24 24" aria-hidden="true"><path d="M3 5h18a1 1 0 0 1 1 1v12a1 1 0 0 1-1 1H3a1 1 0 0 1-1-1V6a1 1 0 0 1 1-1zm9 7.5L20 7H4z"/></svg>
          hello@keystonepp.com
        </li>
        <li>
          <svg viewBox="0 0 24 24" aria-hidden="true"><path d="M12 2a10 10 0 1 0 0 20 10 10 0 0 0 0-20zm6.9 9h-3a15 15 0 0 0-1.3-5.6A8 8 0 0 1 18.9 11zM12 4.1c.9 1.3 1.7 3.6 1.9 6.9h-3.8c.2-3.3 1-5.600 1.9-6.9zM9.4 5.4A15 15 0 0 0 8.1 11h-3a8 8 0 0 1 4.3-5.6zM5.1 13h3a15 15 0 0 0 1.3 5.6A8 8 0 0 1 5.1 13zm6.9 6.9c-.9-1.3-1.7-3.6-1.9-6.9h3.8c-.2 3.3-1 5.6-1.9 6.9zm2.6-1.3a15 15 0 0 0 1.3-5.6h3a8 8 0 0 1-4.3 5.6z"/></svg>
          www.keystonepp.com
        </li>
        <li>
          <svg viewBox="0 0 24 24" aria-hidden="true"><path d="M12 2a7 7 0 0 0-7 7c0 5.2 7 13 7 13s7-7.8 7-13a7 7 0 0 0-7-7zm0 9.5a2.5 2.5 0 1 1 0-5 2.5 2.5 0 0 1 0 5z"/></svg>
          12 Harbour Lane, Eastvale 2041
        </li>
      </ul>
    </div>
    <div class="card__band"></div>
  </section>

</main>
</body>
</html>
```